The Steadfast Compass Method

I need an info graphic that shows how 7 habits help women in senior leadership to Honor Her Past, Steady Mind, and Sharpen Voice - leading to an increased power to influence

https://clipvarn.tv/Qm7RxPz2KaL

7 habits are;

Honest Presence
Trusting Your Inner Voice
Returning To Your Purpose
Restoring Balance
Rethinking
Value Creating
Giving Regard

My Colours are GOLD - BFA55E
White & Black

Fonts Playfair Display & Raleway

The style and feel should be 'high end' luxury quality corporate

Style - luxury

Target Market(s)

Women in senior leadership

Industry/Entity Type

Leadership

Font styles to use
Serif
Sans Serif

Colors
fece3e
fee18a

Requirements
Must have
• style
elegance
contemporary feel
use gold, #BFA55E - black and white creatively

Nice to have
• unusual

```html
<!DOCTYPE html>
<html lang="en">
<head>
<meta charset="utf-8">
<title>The Steadfast Compass Method</title>
<link href="https://fonts.googleapis.com/css2?family=Playfair+Display:wght@400;500&display=swap" rel="stylesheet">
<style>
  :root {
    --cream: #fcfaf3;
    --gold: #bfa55e;
    --gold-fill: rgba(191, 165, 94, 0.45);
    --ink: #1a1a1a;
  }
  * { margin: 0; padding: 0; box-sizing: border-box; }
  html, body { width: 1200px; height: 742px; overflow: hidden; background: var(--cream); }
  .canvas {
    position: relative;
    width: 1200px;
    height: 742px;
    background: var(--cream);
    font-family: "Playfair Display", Georgia, serif;
    color: var(--ink);
  }
  .title {
    position: absolute;
    top: 76px;
    left: 0;
    width: 100%;
    text-align: center;
    font-weight: 400;
    font-size: 57px;
    letter-spacing: 0.5px;
    line-height: 1;
  }
  .framework-diagram {
    position: absolute;
    left: 0;
    top: 0;
    width: 1200px;
    height: 742px;
  }
  .outer-ring { fill: none; stroke: var(--gold); stroke-width: 3; filter: drop-shadow(1px 2px 2px rgba(0,0,0,0.12)); }
  .pillar { fill: var(--gold-fill); }
  .pillar-label { font-family: "Playfair Display", Georgia, serif; font-size: 31px; fill: var(--ink); letter-spacing: 1.5px; }
  .core-label { font-family: "Playfair Display", Georgia, serif; font-size: 24px; fill: var(--ink); }
  .connector { stroke: var(--gold); stroke-width: 3; }
  .connector-dot { fill: var(--gold); }
  .habits-panel {
    position: absolute;
    left: 696px;
    top: 260px;
    width: 350px;
    height: 291px;
    border: 3px solid var(--gold);
    box-shadow: 1px 2px 2px rgba(0,0,0,0.1);
    text-align: center;
  }
  .habits-heading {
    font-weight: 400;
    font-size: 37px;
    line-height: 1;
    margin-top: 22px;
  }
  .habits-list { list-style: none; margin-top: 8px; }
  .habits-list li { font-size: 21px; line-height: 29.6px; }
</style>
</head>
<body>
<main class="canvas">
  <h1 class="title">The Steadfast Compass Method</h1>

  <svg class="framework-diagram" viewBox="0 0 1200 742" aria-label="Three overlapping pillars meeting in a shared centre of lasting impact">
    <defs>
      <path id="arc-past" d="M266.2 446 A80 80 0 0 1 331.1 300.3"/>
      <path id="arc-mind" d="M381.2 306 A80 80 0 0 1 470.3 438.2"/>
      <path id="arc-voice" d="M270.4 489.1 A93 93 0 0 0 455 473"/>
    </defs>

    <circle class="outer-ring" cx="361" cy="406" r="204"/>

    <circle class="pillar" cx="305" cy="376" r="114"/>
    <circle class="pillar" cx="420" cy="376" r="114"/>
    <circle class="pillar" cx="362" cy="473" r="114"/>

    <text class="pillar-label"><textPath href="#arc-past" startOffset="50%" text-anchor="middle">Honor Her Past</textPath></text>
    <text class="pillar-label"><textPath href="#arc-mind" startOffset="50%" text-anchor="middle">Steady Mind</textPath></text>
    <text class="pillar-label"><textPath href="#arc-voice" startOffset="50%" text-anchor="middle">Sharpen Voice</textPath></text>

    <text class="core-label" text-anchor="middle">
      <tspan x="362" y="391">Seat of</tspan>
      <tspan x="362" y="417">Lasting</tspan>
      <tspan x="362" y="443">Impact</tspan>
    </text>

    <line class="connector" x1="566" y1="406" x2="696" y2="406"/>
    <circle class="connector-dot" cx="566" cy="406" r="6"/>
    <circle class="connector-dot" cx="696" cy="406" r="6"/>
  </svg>

  <section class="habits-panel">
    <h2 class="habits-heading">Habits</h2>
    <ul class="habits-list">
      <li>Honest Presence</li>
      <li>Trusting Your Inner Voice</li>
      <li>Returning To Your Purpose</li>
      <li>Restoring Balance</li>
      <li>Rethinking</li>
      <li>Value Creating</li>
      <li>Giving Regard</li>
    </ul>
  </section>
</main>
</body>
</html>
```